Book Cover for nonfiction book about defeating one's grief

I need a book cover (front and back) for a book titled Camino del Alba (Road of the Dawn). I have included a word document of the back cover copy. I liked the design of Where the quiet rivers bend (http://www.pixelvault-studio.com/design/4817293) so something like that would be nice. But if you have a better idea that's fine.
Target Market(s)
People suffering from the loss of a loved one
Requirements
Must have
- Please move the author information (which is the first paragraph) so that it is the last paragraph
- Please include my middle initial in the name (Kevin T. Ashford)
- 6 x 9 inch book, 9mm spine width, 5cm x 3 cm UPC placeholder on back cover
- Thanks!
Nice to have
- should convey relief from grief or some one grieving

```html
<!DOCTYPE html>
<html lang="es">
<head>
<meta charset="utf-8">
<title>Camino del Alba — Cubierta</title>
<link href="https://fonts.googleapis.com/css2?family=Cinzel:wght@400&family=Open+Sans:wght@400&display=swap" rel="stylesheet">
<style>
  :root {
    --ink-white: #ffffff;
    --ink-dark: #1d1d22;
    --panel-dark: rgba(30, 34, 46, 0.86);
    --spine-dark: #23262f;
    --rule: rgba(255, 255, 255, 0.75);
    --sky-light: #eef4f2;
    --sky-blue: #9fc6d0;
    --sun-glow: #fffbe8;
    --field-dark: #1c2418;
    --field-mid: #4a5a3a;
    --barcode-space: #ffffff;
  }
  * { margin: 0; padding: 0; box-sizing: border-box; }
  html, body { width: 1200px; height: 862px; overflow: hidden; background: #ffffff; }

  .cover {
    position: relative;
    width: 1200px;
    height: 862px;
    overflow: hidden;
    font-family: "Open Sans", Arial, sans-serif;
    color: var(--ink-white);
  }

  .cover-photo {
    position: absolute;
    inset: 0;
    background:
      radial-gradient(circle at 990px 215px, var(--sun-glow) 0, rgba(255,250,225,0.9) 60px, rgba(255,245,215,0.35) 170px, rgba(255,245,215,0) 320px),
      radial-gradient(ellipse 90px 250px at 905px 380px, rgba(40,34,44,0.85) 0, rgba(40,34,44,0.6) 70%, rgba(40,34,44,0) 100%),
      linear-gradient(180deg, rgba(0,0,0,0) 0, rgba(0,0,0,0) 300px, rgba(43,53,36,0.85) 400px, var(--field-mid) 500px, var(--field-dark) 862px),
      linear-gradient(100deg, var(--sky-blue) 0, #c9dfe0 35%, var(--sky-light) 70%, #fdf8ea 100%);
  }

  .back-panel {
    position: absolute;
    left: 36px;
    top: 32px;
    width: 494px;
    height: 758px;
    background: var(--panel-dark);
    padding: 0 22px;
  }
  .back-title {
    font-family: "Cinzel", Georgia, serif;
    font-weight: 400;
    font-size: 33px;
    letter-spacing: 1px;
    text-align: center;
    margin-top: 38px;
    line-height: 40px;
  }
  .back-copy {
    font-size: 12.5px;
    line-height: 20.3px;
    text-align: justify;
    hyphens: auto;
  }
  .back-copy--intro { margin-top: 18px; }
  .back-copy--intro p + p { margin-top: 20px; }
  .back-copy--theme { margin-top: 16px; }
  .back-rule {
    width: 390px;
    margin: 0 auto;
    border: 0;
    border-top: 1px solid var(--rule);
  }
  .back-rule--first { margin-top: 24px; }
  .back-rule--second { margin-top: 18px; }
  .author-bio {
    margin-top: 16px;
    font-size: 12.5px;
    line-height: 20.3px;
    text-align: center;
    padding: 0 12px;
  }
  .barcode-space {
    position: absolute;
    left: 282px;
    top: 675px;
    width: 194px;
    height: 113px;
    background: var(--barcode-space);
  }

  .spine {
    position: absolute;
    left: 568px;
    top: 0;
    width: 64px;
    height: 862px;
    background: var(--spine-dark);
  }
  .spine-title, .spine-author {
    position: absolute;
    left: 50%;
    writing-mode: vertical-rl;
    transform: translateX(-50%);
    font-family: "Cinzel", Georgia, serif;
    white-space: nowrap;
  }
  .spine-title { top: 90px; font-size: 39px; letter-spacing: 0.5px; }
  .spine-author { top: 522px; font-size: 31px; letter-spacing: 1.5px; }

  .front-author {
    position: absolute;
    left: 632px;
    width: 568px;
    top: 27px;
    text-align: center;
    font-family: "Cinzel", Georgia, serif;
    font-size: 33px;
    letter-spacing: 2px;
    color: var(--ink-dark);
  }
  .front-title {
    position: absolute;
    left: 632px;
    width: 568px;
    top: 565px;
    text-align: center;
    font-family: "Cinzel", Georgia, serif;
    font-weight: 400;
    line-height: 1;
  }
  .front-title span { display: block; }
  .front-title .title-large { font-size: 88px; }
  .front-title .title-small { font-size: 44px; margin: 6px 0 4px; }
</style>
</head>
<body>
<main class="cover">
  <div class="cover-photo" role="img" aria-label="Fotografía a sangre completa: persona de espaldas con los brazos abiertos en un prado de hierba alta al atardecer, árboles al fondo y el sol brillando con destellos de luz"></div>

  <section class="back-panel">
    <h2 class="back-title">CAMINO DEL ALBA</h2>
    <div class="back-copy back-copy--intro">
      <p>Por miles de años, se le ha dicho a la humanidad que el dolor es una parte necesaria de la vida, y que el profundo dolor después del fallecimiento de nuestros seres queridos es esperado y un proceso natural. Kevin Ashford dice enfáticamente que no, ¡no lo es! Puedes, y deberías estar emocionalmente estable y espiritualmente contento después de la muerte de un ser querido.</p>
      <p>La gente a veces pasa meses o años sumidos en el dolor paralizante, lo cual los aparta de muchos esfuerzos fructíferos. El dolor sabotea las vidas felices y productivas. Algunas veces la gente que trata con dolor extremo o pérdidas, se convierten en personas enojadas, abusan de las drogas y alcohol o incluso de quitan sus propias vidas. No debe ser de esta manera. La tristeza, cuando alguien se va de nuestras vidas, es normal. No es</p>
    </div>
    <hr class="back-rule back-rule--first">
    <p class="back-copy back-copy--theme">La muerte, como parte de la vida, era una norma en la vida de cualquier persona normal. Ahora es raras veces discutida y solo cuando ocurre una emergencia. Camino del Alba es una franca discusión sobre la muerte y morir significa traer paz a los corazones de aquellas personas que están en duelo y esas personas que temen su propia muerte. No es insensible, oscuro y fuerte de leer pero es positivo, reconfortante y espiritualmente tranquilizador.</p>
    <hr class="back-rule back-rule--second">
    <p class="author-bio">Kevin Ashford se graduó de la Universidad Lakeshore Pines y desde entonces ha vivido en Nueva Jersey trabajando como editor y escritor en el mercado de masas, tecnología y los campos de educación. Él es autor de otros tres libros de los que pueden encontrar más en KevinTashford.com</p>
    <div class="barcode-space" aria-label="Espacio reservado para el código UPC"></div>
  </section>

  <aside class="spine">
    <span class="spine-title">CAMINO DEL ALBA</span>
    <span class="spine-author">KEVIN T. ASHFORD</span>
  </aside>

  <p class="front-author">KEVIN T. ASHFORD</p>
  <h1 class="front-title">
    <span class="title-large">CAMINO</span>
    <span class="title-small">DEL</span>
    <span class="title-large">ALBA</span>
  </h1>
</main>
</body>
</html>
```